re brand of Vexawatch.co.uk to Vexawatch.co.uk

We would like a new site design for our Vexawatch.co.uk site

the new domain is Vexawatch.co.uk

we like the blue colour smiler to this site http://www.fundsentrypal.co.uk, and we would like real images o people using instead of cartons

you can take inspiration from the credit ref agency monthly membership site but this product is not a credit report we just like that look

https://www.loanharbor.co.uk
http://www.fundsentrypal.co.uk/
https://www.brimzo.co.uk/

Reason: we have added more details to the project brief and also increased the budget and committed to buying a design

We have guaranteed the project extend the dead line and increased the payment we have also added more details in the brief to give you guys more direction I am looking forward to seeing the designs

Target Market(s)

18 to 50 yo concerned with the privacy and id fraud

The bulk of clients our aged 18 to 30 so a fresh feel is important

Industry/Entity Type

Domain

Colors
33a6d7
0592cd
0555a3
3176b5
85cae6

```html
<!DOCTYPE html>
<html lang="en">
<head>
<meta charset="utf-8">
<title>Vexawatch.co.uk</title>
<link href="https://fonts.googleapis.com/css2?family=Roboto+Condensed:wght@400;700&family=Roboto:wght@400;500&display=swap" rel="stylesheet">
<style>
:root{
  --blue:#33a6d7;
  --blue-deep:#0592cd;
  --blue-soft:#85cae6;
  --blue-head:#6cc0de;
  --ink:#222;
  --muted:#555;
  --darker:#353535;
  --white:#fff;
}
*{box-sizing:border-box;margin:0;padding:0}
html,body{width:1200px;height:3258px;overflow:hidden;background:var(--white)}
body{position:relative;font-family:"Roboto",Arial,sans-serif;color:var(--ink)}
.abs{position:absolute}

/* header */
.site-header{position:absolute;left:0;top:0;width:1200px;height:155px;border-top:5px solid var(--blue-soft)}
.brand{left:109px;top:54px;display:flex;align-items:center;gap:14px}
.brand-mark{width:50px;height:50px;background:var(--blue-soft);border-radius:50%}
.brand-name{font-family:"Roboto Condensed",sans-serif;font-size:38px;color:#333;font-weight:400;white-space:nowrap}
.account-nav{right:110px;top:30px;display:flex;gap:44px;font:700 16px "Roboto Condensed",sans-serif}
.main-nav{right:90px;top:92px;display:flex;align-items:center;font:700 17px "Roboto Condensed",sans-serif}
.main-nav span{padding:0 16px;border-left:1px solid #999;line-height:16px}
.main-nav span:first-child{border-left:0}
.main-nav svg{margin-left:26px}

/* hero */
.hero{left:0;top:155px;width:1200px;height:442px;background:linear-gradient(100deg,#6f7478 0%,#8a8e90 40%,#5a5f63 70%,#3d4145 100%)}
.hero-title{left:0;width:1200px;top:390px;text-align:center;color:var(--white);font:700 42px "Roboto Condensed",sans-serif;letter-spacing:.5px;white-space:nowrap}
.hero-text{left:170px;width:860px;top:450px;text-align:center;color:var(--white);font-size:18px;line-height:26px}
.hero-cta{left:0;width:1200px;top:537px;text-align:center;color:var(--white);font:700 22px "Roboto Condensed",sans-serif}

/* boxed headings */
.boxed{border:2px solid #555;display:flex;align-items:center;justify-content:center;font:700 24px "Roboto Condensed",sans-serif;letter-spacing:1px;white-space:nowrap}
.boxed.light{border-color:var(--white);color:var(--white)}

/* how it works */
.mission{left:120px;width:960px;top:768px;text-align:center;font-size:15px;line-height:24px;color:var(--muted)}
.plan-photo{top:874px;width:285px;height:310px}
.plan{top:1320px;width:320px;text-align:center}
.plan h3{font:700 22px "Roboto Condensed",sans-serif;margin-bottom:22px}
.plan .price{font:700 32px "Roboto Condensed",sans-serif;color:var(--blue);margin-bottom:18px}
.plan p{font-size:14px;line-height:22px;color:var(--muted);height:72px}
.plan .more{font:400 16px "Roboto Condensed",sans-serif;margin-top:14px;letter-spacing:.5px}

/* benefits */
.benefits{left:0;top:1602px;width:1200px;height:635px;background:linear-gradient(160deg,#4a4a4a 0%,#2e2e2e 50%,#3a3a3a 100%)}
.benefit{width:500px;color:var(--white)}
.benefit-head{display:flex;align-items:center;gap:20px;font:700 21px "Roboto Condensed",sans-serif;white-space:nowrap}
.num{width:46px;height:46px;flex:none;background:var(--blue-soft);color:#233;display:flex;align-items:center;justify-content:center;font:700 30px "Roboto Condensed",sans-serif}
.rule{width:54px;height:2px;background:var(--white);margin:4px 0 10px 66px}
.benefit p{font-size:14px;line-height:19px}
.benefit .more{font:700 16px "Roboto Condensed",sans-serif;margin-top:12px}

/* join */
.join-title{left:155px;top:2428px;font:700 22px "Roboto Condensed",sans-serif}
.join-text{left:155px;top:2476px;width:500px;font-size:15px;line-height:24px;color:var(--muted)}
.btn-signup{left:502px;top:2606px;width:150px;height:50px;background:#7fc4dd;color:var(--white);display:flex;align-items:center;justify-content:center;font:700 24px "Roboto Condensed",sans-serif;letter-spacing:1px}
.video{left:720px;top:2438px;width:344px;height:217px;background:linear-gradient(180deg,#2f3136,#1c1d20)}

/* footer */
.footer{left:0;top:2715px;width:1200px;height:367px;background:linear-gradient(180deg,#3e3a39,#2c2a2a)}
.fcol{top:2715px;width:338px;height:316px;background:rgba(70,66,65,.85);color:var(--white);text-align:center}
.fcol h4{height:100px;display:flex;align-items:center;justify-content:center;font:700 25px "Roboto Condensed",sans-serif;background:var(--blue-head)}
.fcol.mid h4{background:#5aa9c6}
.fcol p{font-size:14px;line-height:21px;margin-top:24px;padding:0 40px}
.fbtn{display:inline-block;border:2px solid var(--white);padding:7px 24px;margin-top:14px;font:500 13px "Roboto",sans-serif}
.news-form{display:flex;justify-content:center;margin-top:18px}
.news-form .field{width:195px;height:38px;border:1px solid var(--white)}
.news-form .send{width:70px;height:38px;background:var(--white);color:#333;display:flex;align-items:center;justify-content:center;font:700 14px "Roboto Condensed",sans-serif}

.bottom-bar{left:0;top:3082px;width:1200px;height:81px;background:var(--darker);color:var(--white);font-size:13px}
.copyright{left:95px;top:34px}
.legal{left:468px;top:34px;display:flex;gap:22px}
.social{right:96px;top:28px;display:flex;gap:12px}
.social span{width:24px;height:24px;display:block}
.payments{left:0;top:3163px;width:1200px;height:95px;display:flex;align-items:center;justify-content:center;gap:26px}
.payments span{display:block;background:#d7d7d7}
</style>
</head>
<body>

<header class="site-header">
  <div class="abs brand"><span class="brand-mark"></span><span class="brand-name">VEXAWATCH.CO.UK</span></div>
  <div class="abs account-nav"><span>LOGIN</span><span>SIGNUP</span></div>
  <nav class="abs main-nav">
    <span>HOME</span><span>SOCIAL</span><span>ID ALERT</span><span>BANK ALERT</span><span>CONTACT</span>
    <svg width="14" height="14" viewBox="0 0 14 14"><circle cx="6" cy="6" r="4.5" fill="none" stroke="#333" stroke-width="1.6"/><line x1="9.3" y1="9.3" x2="13" y2="13" stroke="#333" stroke-width="1.8"/></svg>
  </nav>
</header>

<section class="abs hero" role="img" aria-label="Photo of a smiling businessman on the phone in the back seat of a car"></section>
<h1 class="abs hero-title">WE PROTECT YOU EVEN WITHIN YOUR BUSY TIME</h1>
<p class="abs hero-text">We are passionate about helping our members protect themselves in a digital age where criminals no longer fit into the past stereotypes of boogeymen, we're living in an age where you're just as likely to become a victim of theft from someone located across the other side of the world.</p>
<div class="abs hero-cta">TRY IT NOW</div>

<div class="abs boxed" style="left:480px;top:665px;width:240px;height:63px">HOW IT WORKS</div>
<p class="abs mission">Our mission is to help our members protect themselves by equipping them with the tools the digital revolution has brought us in the fight against fraud, whilst at the same time protecting our members from the very risks that come from the digital exposure we all face daily.</p>

<div class="abs plan-photo" style="left:110px;background:linear-gradient(160deg,#c9c9c9,#3c3f44)" role="img" aria-label="Photo of a businessman talking on his mobile phone"></div>
<div class="abs plan-photo" style="left:440px;background:linear-gradient(160deg,#8fb3cf,#dfe6ea)" role="img" aria-label="Photo of hands holding a smartphone"></div>
<div class="abs plan-photo" style="left:771px;background:linear-gradient(160deg,#e6ecef,#8d99a3)" role="img" aria-label="Photo of a customer service agent wearing a headset"></div>

<div class="abs plan" style="left:92px"><h3>BANK ALERT!</h3><div class="price">£15.99</div><p>Adding an extra line of protection between<br>your money and fraudsters.</p><div class="more">READ MORE</div></div>
<div class="abs plan" style="left:423px"><h3>ID ALERT!</h3><div class="price">£15.99</div><p>When the worst has happened speed is<br>of the essence. Be informed at the first possible<br>change with ID ALERTS</p><div class="more">READ MORE</div></div>
<div class="abs plan" style="left:755px"><h3>SOCIAL ALERT!</h3><div class="price">£15.99</div><p>Stop identity theft before it happens.<br>Lorem ipsum dolor si amet omnis aperiam<br>ipsam odit aperiam asperatur.</p><div class="more">READ MORE</div></div>

<section class="abs benefits" role="img" aria-label="Aerial photo of a city at night in dark tones"></section>
<div class="abs boxed light" style="left:448px;top:1697px;width:304px;height:54px">WHAT WE GIVES YOU</div>

<div class="abs benefit" style="left:95px;top:1812px">
  <div class="benefit-head"><span class="num">1</span>IDENTITY FRAUD ALERTS</div><div class="rule"></div>
  <p>Lorem ipsum dolor sit amet voluptatem fugit aut illo omnis explicabo ipsa nemo nam ipsam quasi illo dolores voluptatem doloremque perspiciatis beatae magni architecto odit aspernatur magni quae aperiam</p><div class="more">READ MORE</div>
</div>
<div class="abs benefit" style="left:608px;top:1812px">
  <div class="benefit-head"><span class="num">2</span>WEEKLY IDENTITY REPORTS BY EMAIL OR SMS</div><div class="rule"></div>
  <p>Lorem ipsum dolor sit amet voluptatem fugit aut illo omnis explicabo ipsa nemo nam ipsam quasi illo dolores voluptatem doloremque perspiciatis beatae magni architecto odit aspernatur magni quae aperiam</p><div class="more">READ MORE</div>
</div>
<div class="abs benefit" style="left:95px;top:2021px">
  <div class="benefit-head"><span class="num">3</span>WEEKLY SOCIAL REPORTS BY EMAIL OR SMS</div><div class="rule"></div>
  <p>Lorem ipsum dolor sit amet voluptatem fugit aut illo omnis explicabo ipsa nemo nam ipsam quasi illo dolores voluptatem doloremque perspiciatis beatae magni architecto odit aspernatur magni quae aperiam</p><div class="more">READ MORE</div>
</div>
<div class="abs benefit" style="left:608px;top:2021px">
  <div class="benefit-head"><span class="num">4</span>STOP TELEMARKETING CALLS</div><div class="rule"></div>
  <p>Lorem ipsum dolor sit amet voluptatem fugit aut illo omnis explicabo ipsa nemo nam ipsam quasi illo dolores voluptatem doloremque perspiciatis beatae magni architecto odit aspernatur magni quae aperiam</p><div class="more">READ MORE</div>
</div>

<div class="abs boxed" style="left:252px;top:2319px;width:229px;height:54px">JOIN US NOW</div>
<div class="abs boxed" style="left:768px;top:2319px;width:250px;height:54px">OUR PORTFOLIO</div>
<h3 class="abs join-title">SIGN UP TODAY AND GET PROTECTED</h3>
<p class="abs join-text">Lorem ipsum dolor sit amet rem eos illo omnis aut aperiam ab ipsam ipsa odit sed aperiam aut aspernatur veritatis unde unde, enim accusantium laudantium sunt perspiciatis ipsam sed doloremque ......</p>
<div class="abs btn-signup">SIGN UP</div>
<div class="abs video" role="img" aria-label="Video still of a team of business people standing together"></div>
<svg class="abs" style="left:866px;top:2520px" width="52" height="52" viewBox="0 0 52 52"><circle cx="26" cy="26" r="24" fill="#fff"/><path d="M21 16 L36 26 L21 36 Z" fill="#222"/></svg>

<section class="abs footer"></section>
<div class="abs fcol" style="left:95px">
  <h4>SERVICE TIME</h4>
  <p>Our customer services team is available from <b>9:30am</b> to <b>4:30pm</b> Monday to Friday. Its our goal to answer all enquiries and requests</p>
  <span class="fbtn">READ MORE</span>
</div>
<div class="abs fcol mid" style="left:433px">
  <h4>OUR ADDRESS</h4>
  <p>Vexawatch Harwell House<br>12 Orchard Row, Manchester,<br>M4 7QX, UK.</p>
  <span class="fbtn">FIND IN MAPS</span>
</div>
<div class="abs fcol" style="left:771px">
  <h4>NEWSLETTER</h4>
  <p>Lorem ipsum dolor sit amet omnis aperiam</p>
  <div class="news-form"><span class="field"></span><span class="send">SEND</span></div>
  <p style="margin-top:16px">ab ipsam quasi odit sed aperiam aut aspernatur veritatis unde enim accusantium laudantium</p>
</div>

<footer class="abs bottom-bar">
  <div class="abs copyright">© 2015 <b>VEXAWATCH.CO.UK</b> &nbsp;ALL RIGHTS RESERVED.</div>
  <div class="abs legal"><span>TERMS AND CONDITIONS</span><span>PRIVACY POLICY</span><span>OPT OUT</span></div>
  <div class="abs social">
    <span style="background:#3b5b98"></span><span style="background:#2aa3d8"></span><span style="background:#d23b2f"></span><span style="background:#2d74b0"></span><span style="background:#c62c34"></span>
  </div>
</footer>
<div class="abs payments">
  <span style="width:80px;height:34px"></span>
  <span style="width:90px;height:34px"></span>
  <span style="width:50px;height:34px;border-radius:17px"></span>
  <span style="width:70px;height:34px"></span>
</div>

</body>
</html>
```